Qorvilo IT Website

We need a logo design for a new company in Jeffersonville, IN (serving predminately the Louisville, KY area). We merged Tarnwell Information Systems (an IT staffing company) and Cobalt Wayfarers (a business intelligence consulting group). Our logo was completed through Brush Market. We are doing a soft launch as we want one web page with just basic information and link that to the existing web pages we have: 1) www.tarnwellinfo.com and 2) www.cobaltwayfarers.com.
The 3 tabs we have in mind are:
Services/News/About Us. Under Services are: IT Staffing, Analytics/BI, Strategic Outsourcing, and CIO Services. Under About Us, we have History, Leadership and Contact Us. No submenu for News.
We also want to have the current companies' sites as clickable links. One should be IT Staffing (directed to www.tarnwellinfo.com) and the other should be Business Intelligence/Data Analytics (directed to www.cobaltwayfarers.com).
Target Market(s)
IT professionals and clients needing IT services
Industry/Entity Type
It Company
Coding
Coded - Design and coding required
Number of Pages Required
4 page
Look and feel

```html
<!DOCTYPE html>
<html lang="en">
<head>
<meta charset="utf-8">
<title>Qorvilo IT</title>
<link rel="stylesheet" href="https://fonts.googleapis.com/css2?family=Exo+2:wght@500;600;700&family=Lato:wght@400;700&display=swap">
<style>
:root{
  --blue:#2f95d6;
  --blue-deep:#1f6fae;
  --blue-light:#7ec0ec;
  --navy:#1b4f86;
  --dark:#1f1e23;
  --dark-line:#34333a;
  --text-light:#e8eaee;
  --white:#ffffff;
}
*{margin:0;padding:0;box-sizing:border-box}
html,body{width:1200px;height:3579px;overflow:hidden}
body{position:relative;background:var(--dark);font-family:"Lato",sans-serif;color:var(--text-light)}
.abs{position:absolute}

/* hero */
.hero-band{left:0;top:0;width:1200px;height:966px}
.site-header{left:0;top:0;width:1200px;height:110px}
.brand{left:80px;top:22px;display:flex;align-items:center;gap:14px}
.brand-square{width:52px;height:52px;background:var(--navy);border-radius:6px}
.brand-text{display:flex;flex-direction:column}
.brand-name{font-family:"Exo 2",sans-serif;font-weight:700;font-size:40px;color:var(--navy);line-height:1}
.brand-tag{font-family:"Exo 2",sans-serif;font-weight:600;font-size:12px;color:var(--navy);letter-spacing:.5px;margin-top:2px}
.main-nav{right:80px;top:38px;display:flex;gap:46px}
.main-nav a{font-family:"Exo 2",sans-serif;font-weight:600;font-size:17px;color:#3a3f48;text-decoration:none;letter-spacing:.5px}
.main-nav a.current{color:#111}
.slider-dots{left:543px;top:614px;display:flex;gap:14px}
.slider-dots span{width:26px;height:24px;background:var(--blue-deep)}
.welcome{left:0;top:752px;width:1200px;text-align:center}
.welcome h1{font-family:"Exo 2",sans-serif;font-weight:500;font-size:42px;color:var(--white)}
.welcome p{width:1010px;margin:22px auto 0;font-size:13.5px;line-height:23px;color:var(--white)}

/* service rows */
.divider-v{left:600px;top:966px;width:1px;height:1716px;background:var(--dark-line)}
.divider-h{left:0;width:1200px;height:1px;background:var(--dark-line)}
.service{width:500px}
.service-mark{width:46px;height:46px;border:3px solid var(--blue);border-radius:6px}
.service h2{font-family:"Exo 2",sans-serif;font-weight:700;font-size:40px;color:var(--white);margin-top:28px}
.service p{font-size:18px;line-height:28px;margin-top:12px;color:var(--text-light)}
.service a{display:inline-block;margin-top:22px;font-size:18px;color:var(--blue);text-decoration:none}
.art{background:linear-gradient(135deg,#1e4d78,#2a7fc0 60%,#1d3d5e)}

/* news */
.news-title{left:0;top:2725px;width:1200px;text-align:center;font-family:"Exo 2",sans-serif;font-weight:700;font-size:40px;color:var(--white)}
.news-card{top:2796px;width:335px}
.news-photo{width:335px;height:162px}
.news-body{display:flex;gap:14px;margin-top:14px}
.news-date{flex:none;width:46px;height:58px;background:var(--blue);color:var(--white);text-align:center;font-family:"Exo 2",sans-serif;font-weight:700;line-height:1;padding-top:6px}
.news-date b{display:block;font-size:24px}
.news-date span{font-size:16px}
.news-body h3{font-family:"Exo 2",sans-serif;font-weight:700;font-size:16px;line-height:21px;color:var(--white)}
.news-body p{font-size:14px;line-height:20px;margin-top:6px;color:#c9ccd2}
.news-body a{display:block;margin-top:8px;font-size:15px;color:var(--blue);text-decoration:none}
.news-rule{left:79px;top:3161px;width:1042px;height:1px;background:var(--dark-line)}

/* partners + footer */
.partners{left:0;top:3212px;width:1200px;display:flex;justify-content:center;gap:70px}
.partner{display:flex;align-items:center;gap:10px;font-size:19px;font-weight:700;color:var(--blue);text-decoration:none}
.partner i{width:26px;height:26px;background:var(--blue);display:block}
.footer-wave{left:0;top:3196px;width:1200px;height:383px}
.footer-mark{left:570px;top:3380px;width:60px;height:60px;border:3px solid var(--white);border-radius:8px}
.social{left:523px;top:3464px;display:flex;gap:22px}
.social a{width:44px;height:44px;border:2px solid rgba(255,255,255,.85);border-radius:6px;display:block}
.copyright{left:0;top:3528px;width:1200px;text-align:center;font-size:13px;font-weight:700;color:var(--white)}
</style>
</head>
<body>

<svg class="abs hero-band" viewBox="0 0 1200 966" aria-hidden="true">
  <defs>
    <linearGradient id="heroBlue" x1="0" y1="0" x2="0" y2="1">
      <stop offset="0" stop-color="#8ac7ef"/>
      <stop offset="1" stop-color="#3b9ad9"/>
    </linearGradient>
    <linearGradient id="heroSky" x1="0" y1="0" x2="1" y2="0">
      <stop offset="0" stop-color="#eef3f8"/>
      <stop offset=".45" stop-color="#dfe8f1"/>
      <stop offset="1" stop-color="#bfd6ea"/>
    </linearGradient>
  </defs>
  <rect width="1200" height="966" fill="url(#heroBlue)"/>
  <polygon points="0,0 1200,0 1200,575 560,700 0,573" fill="url(#heroSky)"/>
</svg>
<div class="abs" role="img" aria-label="Businessman holding a tablet with a city skyline blended into his silhouette" style="left:180px;top:0;width:520px;height:690px;background:linear-gradient(180deg,rgba(120,150,180,.35),rgba(60,90,130,.55));clip-path:polygon(20% 0,80% 0,95% 100%,5% 100%)"></div>

<header class="abs site-header">
  <div class="abs brand">
    <div class="brand-square"></div>
    <div class="brand-text">
      <span class="brand-name">Qorvilo IT</span>
      <span class="brand-tag">SMART TALENT, SHARPER DATA</span>
    </div>
  </div>
  <nav class="abs main-nav">
    <a class="current" href="#">HOME</a>
    <a href="#">ABOUT US</a>
    <a href="#">SERVICES</a>
    <a href="#">NEWS</a>
  </nav>
</header>

<div class="abs slider-dots"><span></span><span></span><span></span></div>

<section class="abs welcome">
  <h1>Welcome to Qorvilo IT</h1>
  <p>Lorem Ipsum is simply dummy text of the printing and typesetting industry. Lorem Ipsum has been the industry's standard dummy text ever since the 1500s, when an unknown printer took a galley of type and scrambled it to make a type specimen book. It has survived not only five centuries, but also the leap into electronic typesetting, remaining essentially unchanged. It was popularised in the 1960s with the release of Typeveld sheets containing Lorem Ipsum passages, and more recently with desktop publishing software like Pressline Composer including versions of Lorem Ipsum.</p>
</section>

<div class="abs divider-v"></div>
<div class="abs divider-h" style="top:1400px"></div>
<div class="abs divider-h" style="top:1828px"></div>
<div class="abs divider-h" style="top:2255px"></div>
<div class="abs divider-h" style="top:2682px"></div>

<!-- IT Staffing -->
<article class="abs service" style="left:79px;top:1028px">
  <div class="service-mark"></div>
  <h2>IT Staffing</h2>
  <p>Here at Cobalt Wayfarers, we purpose to provide quality, professionally skilled consultants to our clients. Having been on both sides of the table, Cobalt Wayfarers' management team knows how to find the perfect match with both your company and the resource in mind.</p>
  <a href="http://www.tarnwellinfo.com">DISCOVER MORE</a>
</article>
<div class="abs art" role="img" aria-label="Connected consultant icons in blue tiles" style="left:730px;top:990px;width:350px;height:390px;opacity:.8"></div>

<!-- BI/Analytics -->
<div class="abs art" role="img" aria-label="Analytics chart illustration in blue outlines" style="left:72px;top:1444px;width:360px;height:300px;opacity:.75"></div>
<article class="abs service" style="left:656px;top:1453px">
  <div class="service-mark"></div>
  <h2>BI/Analytics</h2>
  <p>Cobalt Wayfarers has been involved in many different industries in the last 15 years. Retail, Health Care, Banking, and Marketing to name a few, and each provided its unique challenges to our company. And we're glad to say that we passed each one.</p>
  <a href="http://www.cobaltwayfarers.com">DISCOVER MORE</a>
</article>

<!-- Strategic Outsourcing -->
<article class="abs service" style="left:79px;top:1880px">
  <div class="service-mark"></div>
  <h2>Strategic Outsourcing</h2>
  <p>Lorem Ipsum is simply dummy text of the printing and typesetting industry. Lorem Ipsum has been the industry's standard dummy text ever since the 1500s, when an unknown printer took a galley of type and scrambled it to make a type specimen book.</p>
  <a href="#">DISCOVER MORE</a>
</article>
<div class="abs art" role="img" aria-label="Blue cube with play-arrow markers" style="left:718px;top:1868px;width:300px;height:318px;clip-path:polygon(20% 0,100% 18%,100% 78%,65% 100%,0 78%,0 18%)"></div>

<!-- CIO Services -->
<div class="abs art" role="img" aria-label="Scattered tiles with clock, gear, megaphone, calendar and executive icons" style="left:100px;top:2270px;width:480px;height:395px;opacity:.75"></div>
<article class="abs service" style="left:656px;top:2308px">
  <div class="service-mark"></div>
  <h2>CIO Services</h2>
  <p>Lorem Ipsum is simply dummy text of the printing and typesetting industry. Lorem Ipsum has been the industry's standard dummy text ever since the 1500s, when an unknown printer took a galley of type and scrambled it to make a type specimen book.</p>
  <a href="#">DISCOVER MORE</a>
</article>

<!-- News -->
<h2 class="abs news-title">Latest News</h2>

<article class="abs news-card" style="left:79px">
  <div class="news-photo" role="img" aria-label="Team meeting around a laptop in an office" style="background:linear-gradient(135deg,#6b5a4a,#c9c3bb 55%,#4a4640)"></div>
  <div class="news-body">
    <div class="news-date"><b>05</b><span>Apr</span></div>
    <div><h3>Lorem ipsum is simply dummy text of the printing</h3>
    <p>Lorem Ipsum is simply dummy text of the printing and typesetting industry. Lorem Ipsum has been the industry's</p>
    <a href="#">READ MORE</a></div>
  </div>
</article>
<article class="abs news-card" style="left:434px">
  <div class="news-photo" role="img" aria-label="City lights at dusk seen from above" style="background:linear-gradient(160deg,#3d6f9a,#1f3b57 55%,#c88a4a)"></div>
  <div class="news-body">
    <div class="news-date"><b>05</b><span>Apr</span></div>
    <div><h3>Lorem ipsum is simply dummy text of the printing</h3>
    <p>Lorem Ipsum is simply dummy text of the printing and typesetting industry. Lorem Ipsum has been the industry's</p>
    <a href="#">READ MORE</a></div>
  </div>
</article>
<article class="abs news-card" style="left:790px">
  <div class="news-photo" role="img" aria-label="Hands signing papers at a desk" style="background:linear-gradient(135deg,#d9d4cc,#a9a096 60%,#3a3632)"></div>
  <div class="news-body">
    <div class="news-date"><b>05</b><span>Apr</span></div>
    <div><h3>Lorem ipsum is simply dummy text of the printing</h3>
    <p>Lorem Ipsum is simply dummy text of the printing and typesetting industry. Lorem Ipsum has been the industry's</p>
    <a href="#">READ MORE</a></div>
  </div>
</article>

<div class="abs news-rule"></div>

<!-- Footer -->
<svg class="abs footer-wave" viewBox="0 0 1200 383" aria-hidden="true">
  <defs>
    <linearGradient id="footBlue" x1="0" y1="0" x2="0" y2="1">
      <stop offset="0" stop-color="#3b9ad9"/>
      <stop offset="1" stop-color="#8ac7ef"/>
    </linearGradient>
  </defs>
  <rect width="1200" height="383" fill="url(#footBlue)"/>
  <polygon points="0,0 1200,0 1200,8 600,145 0,8" fill="#1f1e23"/>
</svg>

<div class="abs partners">
  <a class="partner" href="http://www.tarnwellinfo.com"><i></i>Tarnwell Information Systems</a>
  <a class="partner" href="http://www.cobaltwayfarers.com"><i></i>Cobalt Wayfarers</a>
</div>

<div class="abs footer-mark"></div>
<nav class="abs social" aria-label="Social links">
  <a href="#" aria-label="Social profile one"></a>
  <a href="#" aria-label="Social profile two"></a>
  <a href="#" aria-label="Social profile three"></a>
</nav>
<p class="abs copyright">© Qorvilo IT - 2016. All Rights Reserved.</p>

</body>
</html>
```